Website for a Psychologist in Private Practice

I need a cool web design for my website: www.drquorvat.com. I would like it to look professional. Keep all the current content and add: Space for video; radio spots (see Velvet Tide Hour Logo below for those); Quick Inquiry; Brindlepost link; 5 star rating on Zunq; a map; reviews from former patients. I am open to suggestions.

Target Market(s)

Those seeking individual and marital counseling.

Industry/Entity Type

Mental Health

Number of Pages Required

1 page

Font styles to use
Sans Serif
Other font styles liked:
• I'm open but no hard to read script

Requirements
Must have
• All the content on my home page with link for video and radio spots. List services and degrees and expertices (pics not necessary).
Nice to have
• A video of me and radio conversations (logo of Velvet Tide Hour radio attached).
Should not have
• Cartoons, comedy, etc.... I don't need pictures of services (marital, depression, etc...) Just list those.

```html
<!DOCTYPE html>
<html lang="en">
<head>
<meta charset="utf-8">
<title>Dr. Marla J. Quorvat – Psychologist</title>
<link href="https://fonts.googleapis.com/css2?family=Cabin:wght@400;500;600&family=Arimo:ital,wght@0,400;0,700;1,400;1,700&display=swap" rel="stylesheet">
<style>
:root{
  --header-dark:#233f63;
  --header-mid:#3d6590;
  --hero-a:#6fa3d3;
  --hero-b:#a9c7e2;
  --sand:#d8b892;
  --sand-light:#e3c9a6;
  --ink:#2a2a2a;
  --ink-soft:#444;
  --ring:#2d7fc1;
  --ring-green:#22a64a;
  --green:#21b24b;
  --dusk-a:#4a4642;
  --dusk-b:#6a5634;
  --blue:#2d7fc1;
  --footer:#262324;
  --footer-text:#e6e6e6;
  --link-gold:#e0a860;
  --line-grey:#c9c9c9;
  --white:#ffffff;
}
*{box-sizing:border-box;margin:0;padding:0}
h1,h2,h3{font-weight:400}
html,body{width:744px;height:1200px;overflow:hidden}
body{position:relative;font-family:"Arimo",Arial,sans-serif;color:var(--ink);background:var(--white)}
.abs{position:absolute}

/* Header */
.site-header{left:0;top:0;width:744px;height:86px;background:linear-gradient(180deg,var(--header-dark),var(--header-mid))}
.portrait{left:87px;top:5px;width:78px;height:78px;border-radius:50%;border:3px solid var(--white);background:radial-gradient(circle at 50% 40%,#e8cf9a,#9a8363)}
.brand-name{left:174px;top:24px;font-family:"Cabin",sans-serif;font-size:24px;font-weight:500;color:var(--white);letter-spacing:.3px}
.brand-license{left:176px;top:55px;font-family:"Cabin",sans-serif;font-size:10px;color:var(--white)}
.call{left:544px;top:32px;color:var(--white);display:flex;gap:6px;align-items:center}
.call small{display:block;font-size:9px}
.call strong{display:block;font-size:13px;font-weight:400;margin-top:2px}

/* Hero */
.hero{left:0;top:86px;width:744px;height:272px;background:linear-gradient(135deg,var(--hero-a),var(--hero-b))}
.hero-tagline{left:88px;top:186px;font-family:"Cabin",sans-serif;font-size:23px;font-weight:500;line-height:33px;color:var(--white);text-shadow:1px 2px 3px rgba(0,0,0,.45)}
.hero-arrow{top:208px;width:24px;height:22px;background:#3a3a3a;display:flex;align-items:center;justify-content:center;border:1px solid #666}
.hero-arrow.prev{left:5px}.hero-arrow.next{left:715px}

/* Expertise */
.expertise{left:0;top:358px;width:744px;height:202px;background:linear-gradient(180deg,var(--sand-light),var(--sand))}
.section-title{font-family:"Cabin",sans-serif;font-size:16px;color:var(--ink-soft)}
.exp-title{left:82px;top:15px}
.exp-license{left:565px;top:19px;font-family:"Cabin",sans-serif;font-size:10px;color:var(--ink-soft)}
.exp-rule{left:82px;top:38px;width:579px;border-top:1px dashed #6b5b45}
.service{width:140px;text-align:center}
.service-icon{width:72px;height:72px;margin:0 auto;border-radius:50%;border:3px solid var(--ring);background:var(--white)}
.service-icon.active{border-color:var(--ring-green)}
.service-name{margin-top:18px;font-family:"Cabin",sans-serif;font-size:11.5px;font-weight:500;line-height:14px;color:var(--ink)}

/* Degrees */
.degrees{left:0;top:560px;width:744px;height:49px;background:var(--green);color:var(--white)}
.degrees-title{left:118px;top:16px;font-family:"Cabin",sans-serif;font-size:14px;font-weight:500}
.degrees-brace{left:204px;top:8px}
.degree{font-size:8.5px;display:flex;gap:5px;align-items:center}

/* Media band */
.media{left:0;top:609px;width:744px;height:225px;background:linear-gradient(180deg,var(--dusk-a),var(--dusk-b))}
.col-title{top:20px;font-family:"Cabin",sans-serif;font-size:15px;color:var(--white)}
.col-rule{top:45px;width:180px;border-top:1px dashed #b8b0a0}
.video-frame{left:82px;top:57px;width:181px;height:137px;border:2px solid #d9d9d9;background:linear-gradient(135deg,#a89670,#4a5a44);display:flex;align-items:center;justify-content:center}
.inquiry-intro{left:288px;top:59px;font-size:7.5px;color:var(--white)}
.field{left:283px;width:180px;background:rgba(255,255,255,.28);font-size:7.5px;color:var(--white);padding:4px 5px}
.submit{left:283px;top:177px;width:68px;height:19px;background:var(--blue);color:var(--white);font-size:9px;font-weight:700;text-align:center;line-height:19px}
.radio-quote{left:483px;top:57px;width:180px;font-size:8.2px;font-style:italic;line-height:13px;color:var(--white)}
.radio-quote .mark{font-size:16px;font-style:normal;line-height:8px;color:#ccc}
.radio-author{left:618px;top:170px;font-size:8.5px;color:var(--white)}
.view-all{left:486px;top:180px;font-size:9px;color:var(--white);text-decoration:underline}

/* Reviews */
.reviews-title{left:0;top:858px;width:744px;text-align:center;font-family:"Cabin",sans-serif;font-size:14px;color:var(--ink)}
.reviews-rule{left:278px;top:881px;width:188px;border-top:1px solid var(--line-grey)}
.reviews-bar{left:350px;top:880px;width:44px;height:3px;background:var(--blue)}
.reviewer{left:89px;top:898px;width:70px;height:70px;border-radius:50%;background:linear-gradient(135deg,#cdb08e,#2d3a4e)}
.review-text{left:172px;top:900px;width:490px;font-size:8px;font-style:italic;line-height:14.6px;text-indent:24px;color:var(--ink)}
.review-sign{left:174px;top:969px;font-size:8px;font-style:italic;font-weight:700}
.read-more{left:563px;top:982px;font-size:8px;color:var(--ink-soft)}
.read-more span{text-decoration:underline}

/* Footer */
.site-footer{left:0;top:1022px;width:744px;height:152px;background:var(--footer);color:var(--footer-text)}
.foot-title{top:16px;font-family:"Cabin",sans-serif;font-size:10px;color:var(--footer-text)}
.foot-rule{top:32px;border-top:1px dashed #777}
.quick-links{left:83px;top:44px;list-style:none;font-size:8px;line-height:13.6px}
.quick-links li:first-child{color:var(--link-gold)}
.badge{top:43px;height:35px}
.badge.one{left:188px;width:88px;background:var(--white);border:1px solid #4a6fb0}
.badge.two{left:283px;width:89px;background:#8aa83a;border:1px solid #c5d88a}
.rating-badge{left:188px;top:92px;width:50px;height:50px;border-radius:6px;background:#c8261e;display:flex;align-items:center;justify-content:center;font-family:"Cabin",sans-serif;font-size:13px;color:var(--white)}
.share-title{left:252px;top:101px;font-family:"Cabin",sans-serif;font-size:10px}
.share-btn{left:252px;top:116px;width:57px;height:18px;background:#3a5a98;border:1px solid #7b95c8;display:flex;align-items:center;gap:4px;padding-left:4px;font-size:8px;color:var(--white)}
.share-btn i{width:9px;height:9px;background:var(--white);display:block}
.contact{left:404px;top:44px;font-size:8px;line-height:11px}
.contact-row{display:flex;margin-bottom:9px}
.contact-row b{width:18px;font-weight:400}
.radio-promo{left:553px;top:24px;width:106px;height:106px;background:linear-gradient(160deg,#d8407e,#5a6a7c);display:flex;align-items:flex-start;justify-content:center;padding-top:4px;font-family:"Cabin",sans-serif;font-size:9px;font-weight:600;color:var(--white)}
.copyright{left:0;top:1174px;width:744px;height:26px;background:var(--blue);color:var(--white);font-size:8px;text-align:center;line-height:26px}
</style>
</head>
<body>

<header class="site-header abs">
  <div class="portrait abs" role="img" aria-label="Portrait photo of Dr. Marla J. Quorvat"></div>
  <h1 class="brand-name abs">Dr. Marla J. Quorvat</h1>
  <p class="brand-license abs">California # PSY20583</p>
  <div class="call abs">
    <svg width="18" height="18" viewBox="0 0 18 18"><circle cx="9" cy="9" r="8" fill="none" stroke="#fff" stroke-width="1"/><path d="M6 5c-1 1 0 4 2 6s4 3 5 2l-1.5-1.5-1.3.7C9 11.5 7.5 10 7 8.8l.7-1.3z" fill="#fff"/></svg>
    <div><small>Call Us Today</small><strong>949-555-0148</strong></div>
  </div>
</header>

<section class="hero abs" role="img" aria-label="Photo of a woman with open arms on a sunny beach facing the sea"></section>
<p class="hero-tagline abs">The Best way to Conquer<br>a problem is to FACE it</p>
<div class="hero-arrow prev abs"><svg width="8" height="10" viewBox="0 0 8 10"><path d="M6 1L2 5l4 4" stroke="#fff" stroke-width="2" fill="none"/></svg></div>
<div class="hero-arrow next abs"><svg width="8" height="10" viewBox="0 0 8 10"><path d="M2 1l4 4-4 4" stroke="#fff" stroke-width="2" fill="none"/></svg></div>

<section class="expertise abs">
  <h2 class="section-title exp-title abs">My Expertise</h2>
  <p class="exp-license abs">California # PSY20583</p>
  <div class="exp-rule abs"></div>
  <div class="service abs" style="left:54px;top:58px"><div class="service-icon active" role="img" aria-label="Icon of a couple"></div><p class="service-name">Dating &amp;<br>Marriage</p></div>
  <div class="service abs" style="left:180px;top:58px"><div class="service-icon" role="img" aria-label="Icon of a family"></div><p class="service-name">Parenting &amp; Professional<br>Relationships</p></div>
  <div class="service abs" style="left:317px;top:58px"><div class="service-icon" role="img" aria-label="Icon of a person juggling tasks"></div><p class="service-name">Life<br>Management</p></div>
  <div class="service abs" style="left:437px;top:58px"><div class="service-icon" role="img" aria-label="Icon of two faces"></div><p class="service-name">Personality<br>Disorders</p></div>
  <div class="service abs" style="left:550px;top:58px"><div class="service-icon" role="img" aria-label="Icon of a seated figure with head down"></div><p class="service-name">Depression &amp;<br>Anxiety Issues</p></div>
</section>

<section class="degrees abs">
  <h2 class="degrees-title abs">My Degrees</h2>
  <svg class="degrees-brace abs" width="12" height="34" viewBox="0 0 12 34"><path d="M2 1c5 0 5 3 5 8s0 7 4 8c-4 1-4 3-4 8s0 8-5 8" stroke="#fff" stroke-width="1.3" fill="none" opacity=".8"/></svg>
  <p class="degree abs" style="left:239px;top:13px"><svg width="9" height="8" viewBox="0 0 9 8"><path d="M1 4l2.5 3L8 1" stroke="#fff" stroke-width="1.5" fill="none"/></svg>Doctoral Degree in Clinical Psychology</p>
  <p class="degree abs" style="left:239px;top:29px"><svg width="9" height="8" viewBox="0 0 9 8"><path d="M1 4l2.5 3L8 1" stroke="#fff" stroke-width="1.5" fill="none"/></svg>Masters Degree in Counseling Psychology</p>
  <p class="degree abs" style="left:436px;top:13px"><svg width="9" height="8" viewBox="0 0 9 8"><path d="M1 4l2.5 3L8 1" stroke="#fff" stroke-width="1.5" fill="none"/></svg>Doctoral Internship, Halvern Medical Center</p>
  <p class="degree abs" style="left:436px;top:29px"><svg width="9" height="8" viewBox="0 0 9 8"><path d="M1 4l2.5 3L8 1" stroke="#fff" stroke-width="1.5" fill="none"/></svg>Masters Internship, Tessford Clinic</p>
</section>

<section class="media abs" role="img" aria-label="Background photo of a wheat field at sunset">
  <h2 class="col-title abs" style="left:82px">View Video</h2>
  <div class="col-rule abs" style="left:82px"></div>
  <div class="video-frame abs" role="img" aria-label="Video still of Dr. Marla J. Quorvat">
    <svg width="20" height="20" viewBox="0 0 20 20"><circle cx="10" cy="10" r="8.5" fill="none" stroke="#fff" stroke-width="1.5"/><path d="M8 6l5 4-5 4z" fill="#fff"/></svg>
  </div>

  <h2 class="col-title abs" style="left:283px">Quick Inquiry</h2>
  <div class="col-rule abs" style="left:283px"></div>
  <p class="inquiry-intro abs">Lorem ipsum dolor sit amet, consectetuer</p>
  <div class="field abs" style="top:75px;height:19px">Name</div>
  <div class="field abs" style="top:97px;height:19px">Email</div>
  <div class="field abs" style="top:119px;height:19px">Phone</div>
  <div class="field abs" style="top:141px;height:30px">Message</div>
  <div class="submit abs">SUBMIT</div>

  <h2 class="col-title abs" style="left:483px">Radio Conversations</h2>
  <div class="col-rule abs" style="left:483px"></div>
  <p class="radio-quote abs"><span class="mark">“</span> Lorem ipsum dolor sit ae onsecte iscingrd elit, sed diam nonummy nibh euis tincidunt ut laoreetlore gna aliquam erat olutpat. Ut wisi fd enim adinim veniam, quis strud xerc ullamrper suscipit lobortis sal wisi ut laoreetlorna aliquam erat olutpat. Utnim adinim veniam, quis strud a xerci gna aliquam erat olutpat. Ut uis strud fd xerci gna aliquam erat olutpat. Utorem.</p>
  <p class="radio-author abs">Nora Pell</p>
  <p class="view-all abs">View All</p>
</section>

<h2 class="reviews-title abs">Reviews From Former Patients</h2>
<div class="reviews-rule abs"></div>
<div class="reviews-bar abs"></div>
<div class="reviewer abs" role="img" aria-label="Photo of a former patient"></div>
<p class="review-text abs">Lorem ipsum dolor sit amet, consectetuer adipiscing elit, sed diam nonummy nibh euismod tincidunt ut laoreet dolore magna aliquam erat volutpat. Ut wisi enim ad minim veniam, quis nostrud exerci tation ullamcorper suscipit lobortis nisl ut aliquip commodo consequat. Duis autem vel eum iriure dolor in hendrerit in vulputate velit esse molestie consequat, vel illum dolore eu feugiat nulla facilisis at vero eros et accumsan et iusto odio dignissimaugue duis dolore te feugait nulla facilisi.</p>
<p class="review-sign abs">.... Lorem Ispum, Manger</p>
<p class="read-more abs"><span>Read more testimonials</span> »</p>

<footer class="site-footer abs">
  <h3 class="foot-title abs" style="left:83px">Quick Links</h3>
  <div class="foot-rule abs" style="left:83px;width:72px"></div>
  <ul class="quick-links abs">
    <li>Home</li><li>About Me</li><li>Sessions</li><li>Resources</li><li>BIO</li><li>Customer Reviews</li><li>Contact Me</li>
  </ul>

  <h3 class="foot-title abs" style="left:188px">A Portion of All Revenue is Donated to</h3>
  <div class="foot-rule abs" style="left:188px;width:184px"></div>
  <div class="badge one abs" role="img" aria-label="Partner charity badge"></div>
  <div class="badge two abs" role="img" aria-label="Partner charity badge"></div>
  <div class="rating-badge abs">Zunq</div>
  <p class="share-title abs">Brindlepost share</p>
  <div class="share-btn abs"><i></i>SHARE</div>

  <h3 class="foot-title abs" style="left:404px">Contact Details</h3>
  <div class="foot-rule abs" style="left:404px;width:118px"></div>
  <div class="contact abs">
    <div class="contact-row" style="margin-bottom:13px"><b>A:</b><span>417 Larkmoor Street, Suite 210<br>Elmridge Bay, CA 92700</span></div>
    <div class="contact-row"><b>P:</b><span>949-555-0148</span></div>
    <div class="contact-row"><b>TF:</b><span>949-555-0148</span></div>
    <div class="contact-row"><b>E:</b><span>mq@drquorvat.com</span></div>
  </div>

  <div class="radio-promo abs" role="img" aria-label="Velvet Tide Hour radio show promo photo">Velvet Tide Hour</div>
</footer>

<div class="copyright abs">Copyright © 2016 Dr. Marla J. Quorvat&nbsp; All rights reserved</div>

</body>
</html>
```